"MEET THE TEAM" page web design

We need a "meet the team" page for our website!
Please look at our website to see the style we need

We are looking for something unique, fun, cool, technology-style and yet professional. We plan on taking a picture of each employee (not sure if this will be a real photo/caricature/ black and white/goofy picture--> but we are open to any ideas you have that will work with the design) and putting it there, along with a little bio about each person.

Thanks! looking forward to working together:)
Updates

Project Deadline Extended
Reason: I am excited to see more designs and find the perfect fit. Thanks designers :)

Target Market(s)

People looking to purchase servers, workstations, components

Industry/Entity Type

Information Technology

Number of Pages Required

1 page

Font styles to use
Sans Serif
Other font styles liked:
• The font we use on our site so it matches

Requirements
Must have
• please look at our website quenditrex.com and see the theme and colors we want.
• We have 13 employees but would like to have a design where we can add/remove people if we hire/terminate them without messing up the design.
• We are looking for something unique, fun, cool, technology-style and yet professional. We plan on taking a picture of each employee (not sure if this will be a real photo/caricature/ black and white/goofy picture--> but we are open to any ideas you have that will work with the design) and putting it there, along with a little bio about each person.
• We can upload anything you need
Nice to have
• We are also interested in having a design where when the cursor moves over a person then the bio comes out or moves around, or something. (This is not required, but we would love some cool ideas) And if you can come up with some design, we would have our programmers create it for us.
Should not have
• we are open to anything

```html
<!DOCTYPE html>
<html lang="en">
<head>
<meta charset="utf-8">
<title>Quenditrex – Team</title>
<link href="https://fonts.googleapis.com/css2?family=Roboto:wght@400;500;700&display=swap" rel="stylesheet">
<style>
  :root{
    --teal:#2fc1b1;
    --teal-light:#42d6c6;
    --text:#3a3a3a;
    --muted:#6b6b6b;
    --line:#e3e3e3;
    --panel:#f3f3f3;
    --navy:#2c2f45;
    --tab:#a8a8a8;
    --white:#ffffff;
  }
  *{box-sizing:border-box;margin:0;padding:0}
  html,body{width:1200px;height:1000px;overflow:hidden;background:var(--white);font-family:"Roboto",Arial,sans-serif;color:var(--text)}
  .page{position:relative;width:1200px;height:1000px;overflow:hidden}

  /* header */
  .brand{position:absolute;left:63px;top:32px;display:flex;align-items:center;gap:14px}
  .brand-dot{width:34px;height:34px;border-radius:50%;background:var(--teal)}
  .brand-name{font-size:34px;font-weight:500;letter-spacing:2px;color:var(--teal)}
  .account-tab{position:absolute;left:945px;top:0;width:195px;height:34px;background:var(--tab);border-radius:0 0 34px 0;display:flex;align-items:center;padding-left:30px;gap:34px;font-size:13px;color:#3a3a3a}
  .contact{position:absolute;top:48px;display:flex;align-items:center;gap:10px}
  .contact-chat{left:832px}
  .contact-phone{left:1000px}
  .contact-icon{width:42px;height:42px;border-radius:50%;border:1px solid var(--line);display:flex;align-items:center;justify-content:center;box-shadow:0 1px 3px rgba(0,0,0,.12)}
  .contact-chat .label{font-size:14px;color:var(--muted);margin-top:10px}
  .contact-phone .label{font-size:20px;color:#333}

  .nav{position:absolute;left:0;top:101px;width:1200px;height:46px;border-top:1px solid var(--line);display:flex;align-items:center}
  .nav-links{display:flex;gap:27px;margin-left:63px;font-size:12.5px;color:#555;list-style:none;letter-spacing:.2px}
  .search{position:absolute;left:1000px;top:8px;width:162px;height:32px;border:1px solid #cfcfcf;border-radius:16px;display:flex;align-items:center;justify-content:space-between;padding:0 10px 0 18px;font-size:12px;color:#444;box-shadow:0 1px 2px rgba(0,0,0,.1)}
  .cart{position:absolute;left:1170px;top:6px;width:38px;height:38px;border-radius:50%;border:1px solid #cfcfcf;display:flex;align-items:center;justify-content:center}

  .crumb-rule{position:absolute;left:0;top:148px;width:1200px;height:3px;background:var(--teal)}
  .crumb{position:absolute;left:0;top:153px;width:1200px;height:36px;background:linear-gradient(90deg,var(--teal),var(--teal-light) 60%,var(--teal));padding-left:131px;display:flex;align-items:center;font-size:13px;color:var(--white)}
  .crumb b{color:#16373a;font-weight:700}

  /* team grid */
  .team{position:absolute;left:122px;top:234px;display:grid;grid-template-columns:repeat(4,218px);column-gap:27px;row-gap:29px}
  .card{position:relative;width:218px;height:300px;border-bottom:4px solid var(--navy);overflow:hidden}
  .photo{position:absolute;left:0;top:0;width:218px;height:296px}
  .info{position:absolute;left:0;bottom:0;width:218px;height:106px;background:var(--panel);clip-path:polygon(0 0,100% 46px,100% 100%,0 100%)}
  .info .name{position:absolute;left:16px;top:62px;font-size:14.5px;color:#333}
  .info .role{position:absolute;left:16px;top:81px;font-size:12px;color:var(--muted)}

  .card.is-open{border-bottom-color:var(--teal)}
  .card.is-open .info{height:208px;clip-path:polygon(0 62px,100% 0,100% 100%,0 100%)}
  .vertical-id{position:absolute;left:14px;bottom:10px;transform-origin:left bottom;transform:rotate(-90deg) translate(0,100%);white-space:nowrap;line-height:1.15}
  .vertical-id .v-name{display:block;font-size:14px;color:var(--teal)}
  .vertical-id .v-role{display:block;font-size:12px;color:#444}
  .detail{position:absolute;left:72px;display:flex;align-items:center;gap:12px;font-size:12px;color:#444}
  .detail-phone{top:131px}
  .detail-mail{top:154px}
  .socials{position:absolute;left:72px;top:186px;display:flex;gap:30px}
  .socials span{width:7px;height:7px;border-radius:50%;background:#555}

  .row-2 .info .name{top:62px}
</style>
</head>
<body>
<div class="page">

  <header>
    <div class="brand"><span class="brand-dot"></span><span class="brand-name">QUENDITREX</span></div>
    <div class="account-tab"><span>SIGN UP</span><span>LOGIN</span></div>
    <div class="contact contact-chat">
      <span class="contact-icon">
        <svg width="18" height="16" viewBox="0 0 18 16"><path d="M2 1h11a2 2 0 0 1 2 2v6a2 2 0 0 1-2 2H7l-4 3v-3H2a2 2 0 0 1-2-2V3a2 2 0 0 1 2-2z" fill="#2fc1b1"/></svg>
      </span>
      <span class="label">LIVE CHAT</span>
    </div>
    <div class="contact contact-phone">
      <span class="contact-icon">
        <svg width="16" height="16" viewBox="0 0 16 16"><path d="M3 1l3 3-2 2c1 2 3 4 6 6l2-2 3 3-2 2C7 15 1 9 1 3z" fill="#2fc1b1"/></svg>
      </span>
      <span class="label">555-014-2290</span>
    </div>
  </header>

  <nav class="nav">
    <ul class="nav-links">
      <li>SERVERS</li><li>WORKSTATIONS</li><li>COMPONENTS</li><li>VIRTUAL REALITY</li><li>DRONES</li><li>ABOUT US</li><li>BLOG</li><li>RESOURCES</li><li>CONTACT US</li>
    </ul>
    <div class="search"><span>Search</span>
      <svg width="14" height="14" viewBox="0 0 14 14"><circle cx="6" cy="6" r="4.5" fill="none" stroke="#2fc1b1" stroke-width="2"/><path d="M9.5 9.5l3.5 3.5" stroke="#2fc1b1" stroke-width="2"/></svg>
    </div>
    <div class="cart">
      <svg width="18" height="16" viewBox="0 0 18 16"><path d="M1 6h16l-2 9H3z" fill="#2fc1b1"/><path d="M5 6l4-5 4 5" fill="none" stroke="#2fc1b1" stroke-width="1.6"/></svg>
    </div>
  </nav>

  <div class="crumb-rule"></div>
  <div class="crumb">HOME&nbsp;/&nbsp;<b>TEAM</b></div>

  <main class="team">
    <article class="card">
      <div class="photo" role="img" aria-label="Portrait of the founder in glasses and a blue shirt" style="background:linear-gradient(160deg,#3b3f45,#4f6079 60%,#6b5e3c)"></div>
      <div class="info"><span class="name">Dorian Castell</span><span class="role">CEO / Founder</span></div>
    </article>

    <article class="card is-open">
      <div class="photo" role="img" aria-label="Portrait of the head of design in a leather jacket" style="background:linear-gradient(160deg,#c8ad7c,#8a7352 55%,#3a3230)"></div>
      <div class="info">
        <div class="vertical-id"><span class="v-name">Rowan Aldis</span><span class="v-role">Head of Design</span></div>
        <div class="detail detail-phone">
          <svg width="11" height="11" viewBox="0 0 16 16"><path d="M3 1l3 3-2 2c1 2 3 4 6 6l2-2 3 3-2 2C7 15 1 9 1 3z" fill="#2fc1b1"/></svg>
          <span>+1555&nbsp; 014&nbsp; 772</span>
        </div>
        <div class="detail detail-mail">
          <svg width="12" height="9" viewBox="0 0 12 9"><rect width="12" height="9" rx="1" fill="#2fc1b1"/><path d="M0 1l6 4 6-4" fill="none" stroke="#fff" stroke-width="1"/></svg>
          <span>team@quenditrex.com</span>
        </div>
        <div class="socials" aria-label="Social profiles"><span></span><span></span><span></span><span></span></div>
      </div>
    </article>

    <article class="card">
      <div class="photo" role="img" aria-label="Portrait of a team member in a striped shirt" style="background:linear-gradient(160deg,#c9cacc,#8f9196 55%,#2e2f33)"></div>
      <div class="info"><span class="name">Elias Marwood</span><span class="role">Member</span></div>
    </article>

    <article class="card">
      <div class="photo" role="img" aria-label="Portrait of a team member in a denim jacket" style="background:linear-gradient(160deg,#4b5a3a,#6f7a5a 45%,#3e5f8a)"></div>
      <div class="info"><span class="name">Corwin Haltby</span><span class="role">Member</span></div>
    </article>

    <article class="card row-2">
      <div class="photo" role="img" aria-label="Portrait of a team member in sunglasses and a waistcoat" style="background:linear-gradient(160deg,#9fc3e6,#8c6a4e 55%,#e8e8e8)"></div>
      <div class="info"><span class="name">Lucan Ferreby</span></div>
    </article>

    <article class="card row-2">
      <div class="photo" role="img" aria-label="Portrait of a team member in a denim shirt" style="background:linear-gradient(160deg,#c3ccd4,#51657d 55%,#2f3c4f)"></div>
      <div class="info"><span class="name">Jasper Noleth</span></div>
    </article>

    <article class="card row-2">
      <div class="photo" role="img" aria-label="Portrait of a bearded team member in a black sweater" style="background:linear-gradient(160deg,#b9b8b3,#7d7b76 50%,#1f1f22)"></div>
      <div class="info"><span class="name">Theron Vale</span></div>
    </article>

    <article class="card row-2">
      <div class="photo" role="img" aria-label="Portrait of a smiling team member in a suit" style="background:linear-gradient(160deg,#e6eef4,#b7c8d6 50%,#2b3a55)"></div>
      <div class="info"><span class="name">Marek Dunstall</span></div>
    </article>
  </main>

</div>
</body>
</html>
```